world's hottest chilli salt 7 flavours

I am needing a packaging design for 7 different ones to reflect our range

We are located in Perth OZ. Our chilli salts are new and unique and the world’s hottest ones as we use the world’s hottest chillies. Our product is made from chilli and salts but then other flavours to make them different - one for example is a Smokey one which is very popular and it made from salt, chilli, chipotle, coriander, yellow mustard seeds and garlic.

the colour distinguishes the difference between the different flavours

ingredient list is on the website for each flavour
please view fernmoltaskel.com at our range of chilli salts

Target Market(s)

Male adults age is from 18 + - target market is Australian market but will be selling overseas as well to the US.

Industry/Entity Type

Product

Requirements
Must have
• must be colour code as examples i have uploaded whether or to view fernmoltaskels.com -it it bigger or small i'm not fussed but there needs to be a distinction between the 7 different flavours. Size of label is 95mm x 37mm to work from so very small. The relish the blaze (attached) needs to be somewhere on the logo but i would like to see what someone can do with that.
the logo is found with the tongue attached - this is needed and to be quite big if possible – we need the chilli image. It needs to be a good design where our customers and us go WOW.

text of the salts is found on the website.

barcode is needed along the right side. but do not include in the image i will put that on myself

also ingredient list - this is currently not looking any good.

needs to be the "worlds hottest" somewhere
Nice to have
• something clean crisp and elegant like

http://crateloomviews.examplehost.net/2009/10/plain-drop.html

** this is what we would like http://3.img.examplehost.net/_9QwLrTzXpaM/RkPd-7NnvGs/AAAAAAAAH2K/kTr4WZxeLPQ/s1600/KLMV+cards.jpg
clean crisp and
Should not have
• too many fonts

```html
<!DOCTYPE html>
<html lang="en">
<head>
<meta charset="utf-8">
<title>Very Hot Bhut Jolokia Chilli Salt Label</title>
<link href="https://fonts.googleapis.com/css2?family=Julius+Sans+One&family=Smokum&family=Roboto+Condensed:wght@400&display=swap" rel="stylesheet">
<style>
  :root {
    --blue-glow: #2e86c8;
    --blue-mid: #1f4f9a;
    --navy: #272062;
    --yellow: #f6ee1e;
    --white: #ffffff;
    --black: #151515;
    --tag-blue: #2b4f9e;
    --ink-grey: #3a3a3a;
  }
  html, body {
    margin: 0;
    padding: 0;
    width: 1200px;
    height: 467px;
    overflow: hidden;
    background: var(--navy);
  }
  .label {
    position: relative;
    width: 1200px;
    height: 467px;
    overflow: hidden;
    background: radial-gradient(ellipse 560px 300px at 620px 250px, var(--blue-glow) 0%, var(--blue-mid) 45%, var(--navy) 100%);
    font-family: "Roboto Condensed", Arial, sans-serif;
  }
  .ingredients-tab {
    position: absolute;
    left: 21px;
    top: 225px;
    width: 27px;
    height: 214px;
    background: var(--black);
  }
  .ingredients-tab span {
    position: absolute;
    left: 50%;
    top: 50%;
    transform: translate(-50%, -50%) rotate(-90deg);
    font-family: "Julius Sans One", sans-serif;
    font-size: 15px;
    letter-spacing: 4px;
    color: var(--ink-grey);
    white-space: nowrap;
  }
  .ingredients-list {
    position: absolute;
    left: 86px;
    top: 439px;
    width: 396px;
    transform-origin: 0 0;
    transform: rotate(-90deg);
    margin: 0;
    color: var(--white);
    font-size: 14px;
    line-height: 17px;
  }
  .brand-mark {
    position: absolute;
    left: 321px;
    top: 43px;
    width: 150px;
    height: 180px;
    background: var(--white);
    border-radius: 10px;
  }
  .brand-name {
    position: absolute;
    left: 490px;
    top: 32px;
    margin: 0;
    font-family: "Julius Sans One", sans-serif;
    font-weight: 400;
    font-size: 48px;
    line-height: 74px;
    letter-spacing: 9px;
    color: var(--white);
  }
  .product-name {
    position: absolute;
    left: 0;
    top: 0;
    margin: 0;
    font-family: "Smokum", serif;
    font-weight: 400;
    color: var(--yellow);
    line-height: 1;
  }
  .product-name span { position: absolute; white-space: nowrap; }
  .line-very-hot { left: 503px; top: 200px; font-size: 62px; }
  .line-bhut { left: 468px; top: 252px; font-size: 92px; }
  .line-salt { left: 487px; top: 334px; font-size: 68px; }
  .tagline {
    position: absolute;
    left: 439px;
    top: 406px;
    width: 369px;
    height: 33px;
    margin: 0;
    background: var(--black);
    color: var(--tag-blue);
    font-family: "Julius Sans One", sans-serif;
    font-size: 19px;
    letter-spacing: 3px;
    line-height: 33px;
    text-align: center;
  }
</style>
</head>
<body>
  <div class="label">
    <div class="ingredients-tab"><span>INGREDIENTS</span></div>
    <p class="ingredients-list">Bhut Jolokia Chilli, Pink Himalayan Rock Salt, Onion, Garlic, Thyme, Pepper, Mustard Seed, Coriander and more!</p>

    <div class="brand-mark" aria-hidden="true"></div>
    <h1 class="brand-name">FERN<br>MOLTASKEL</h1>

    <h2 class="product-name">
      <span class="line-very-hot">Very Hot</span>
      <span class="line-bhut">Bhut Jolokia</span>
      <span class="line-salt">Chilli Salt</span>
    </h2>

    <p class="tagline">THE/WORLD'S/HOTTEST!</p>
  </div>
</body>
</html>
```